Transfer Tortoise - Cloud Based Data Migration Service for IT Professionals

We are looking for a smart clean website design for an informational site about our services and as a main portal into the service itself. We would like the design completed in WORDPRESS so that it will easily connect with the service.

Transfer Tortoise is a cloud based migration service providing (to start with) a online migration tool that we migrate Kelvarn Postbox mailboxes (email) with all the settings, attachments from one system to another.
The service is aimed at IT professionals, IT companies and IT departments so our customers will be very technology based.

The Service -
IT companies currently migrate email; data and databases. using a very time intensive process which is both expensive and means their customer potentially losses access to its IT for a significant period of time. Additionally there are risks with regards to compatibility between systems and loss of data.
Potential benefits include;
• cost savings
• improved customer service, including reduced downtime
• improved resilience of the process
We are therefore developing cloud based migration software/website which will automate the process, mitigating these issues, as well as providing additional benefits such as the ability to sort and migrate only certain areas of data or certain emails, to check the integrity of the data/emails moved and to also repair corrupted data and emails.
The system will effectively duplicate the data and emails onto the new system over the weeks prior to the completion date. This will enable the IT Company to complete a final synchronisation and then immediately switch over to the new system with no interruption to the end users.
There is also an added benefit that the end users can test the system (with their own data and emails) prior to the switch over date to ensure everything is in place and databases work correctly.
The system will be completely cloud based and therefore easy for the IT Companies to access. They will be able to purchase the use of the system using CoinDrift or credit card and will only need to purchase what they need, this will allow even small local IT companies the facilities which previously would have been cost prohibitive to them.

Some of the sites we like for reference are -
Trellward, brightlots, the sky shuttler.

We already have a logo design see attached and the website will need to work with this design.
Please message me if you have any questions
We do have the logo in other file formats if required.
Many Thanks

Target Market(s)

IT Sector

Industry/Entity Type

It Service

Number of Pages Required

5+ page

Requirements
Must have
• Front Page
• About Us
• Contact Info
• Blog
• Benefits
• More Information
• Must be Mobile Phone Compatible/friendly
• Log in (button) and support button on all pages (possibley top right)

```html
<!DOCTYPE html>
<html lang="en">
<head>
<meta charset="utf-8">
<title>Transfer Tortoise – Cloud Based Email Migration</title>
<link href="https://fonts.googleapis.com/css2?family=Raleway:wght@300;400;500;600;700&family=Open+Sans:wght@400;600&display=swap" rel="stylesheet">
<style>
:root{
  --blue:#1a9ee4;
  --blue-light:#4fbdf2;
  --blue-deep:#0d4f86;
  --navy:#0b3e6c;
  --orange:#f39c12;
  --ink:#555b61;
  --ink-soft:#8a9097;
  --grey-bg:#eeeff1;
  --footer:#2b2b2d;
  --footer-text:#a9abaf;
  --white:#ffffff;
}
*{box-sizing:border-box;margin:0;padding:0}
html,body{width:1200px;height:2164px;overflow:hidden;background:var(--white)}
body{position:relative;font-family:"Open Sans",Arial,sans-serif;color:var(--ink)}
h1,h2,h3,.brand-name{font-family:"Raleway",Arial,sans-serif}

/* header */
.site-header{position:absolute;left:0;top:0;width:1200px;height:60px;background:var(--white);box-shadow:0 1px 3px rgba(0,0,0,.08);z-index:5}
.brand{position:absolute;left:180px;top:16px;display:flex;align-items:center;gap:10px}
.brand-dot{width:28px;height:28px;border-radius:50%;background:var(--blue)}
.brand-name{font-size:20px;font-weight:600;color:var(--blue-deep);letter-spacing:.5px}
.main-nav{position:absolute;left:470px;top:22px;display:flex;gap:26px;font-family:"Raleway",sans-serif;font-size:11px;font-weight:600;color:#6d7379;letter-spacing:.5px}
.main-nav .active{color:var(--blue)}
.btn-support,.btn-login{position:absolute;top:17px;height:26px;padding:0 16px;font-family:"Raleway",sans-serif;font-size:11px;font-weight:700;color:var(--white);line-height:26px;border-radius:2px;letter-spacing:.5px}
.btn-support{left:855px;background:var(--orange)}
.btn-login{left:945px;background:var(--blue)}

/* hero */
.hero{position:absolute;left:0;top:60px;width:1200px;height:470px;background:linear-gradient(180deg,var(--blue) 0%,var(--blue-light) 100%);overflow:hidden}
.hero-title{position:absolute;left:180px;top:110px;color:var(--white);font-weight:300;line-height:1.25}
.hero-title .line1{display:block;font-size:30px}
.hero-title .line2{display:block;font-size:38px}
.hero-copy{position:absolute;left:180px;top:218px;width:320px;color:#e3f4fd;font-size:11px;line-height:1.6}
.btn-outline{position:absolute;height:28px;padding:0 16px;border:1px solid var(--white);color:var(--white);font-family:"Raleway",sans-serif;font-size:11px;font-weight:600;line-height:26px;border-radius:2px}
.hero .btn-outline{left:180px;top:285px}
.hero-laptop{position:absolute;left:600px;top:95px;width:300px;height:200px;border-radius:10px 10px 4px 4px;background:linear-gradient(180deg,#dfe6ec,#9aa7b3)}
.hero-planes{position:absolute;left:920px;top:150px;width:110px;height:70px;background:linear-gradient(135deg,rgba(255,255,255,.75),rgba(214,236,250,.3));border-radius:4px}
.cloud-bank{position:absolute;left:0;bottom:0;width:1200px;height:150px;background:linear-gradient(180deg,rgba(255,255,255,0) 0%,rgba(255,255,255,.85) 55%,#ffffff 100%)}

/* features */
.features{position:absolute;left:0;top:530px;width:1200px;height:260px;background:var(--white)}
.feature{position:absolute;top:20px;width:240px;text-align:center}
.feature-icon{width:76px;height:76px;margin:0 auto;border-radius:50%;border:2px solid #d4d8dc;display:flex;align-items:center;justify-content:center}
.feature h3{margin-top:16px;font-size:16px;font-weight:500;color:#43484d}
.feature p{margin-top:8px;font-size:10px;line-height:1.6;color:var(--ink-soft)}

/* migrate */
.migrate{position:absolute;left:0;top:790px;width:1200px;height:370px;background:linear-gradient(180deg,var(--navy),var(--blue-deep))}
.migrate h2{position:absolute;left:190px;top:90px;font-size:28px;font-weight:400;color:var(--white)}
.migrate p{position:absolute;left:190px;width:420px;font-size:10.5px;line-height:1.6;color:#c5d8ea}
.migrate .btn-outline{left:190px;top:272px}
.migrate-screen{position:absolute;left:730px;top:55px;width:250px;height:255px;border-radius:6px;background:linear-gradient(180deg,#e9eef2,#aab5bf)}

/* how it works */
.how{position:absolute;left:0;top:1160px;width:1200px;height:370px;background:var(--white)}
.how-diagram{position:absolute;left:160px;top:55px;width:380px;height:270px;border-radius:40px;background:radial-gradient(ellipse at 50% 35%,#8fd4f7 0%,#cdebfa 55%,#ffffff 80%)}
.how h2{position:absolute;left:620px;top:95px;font-size:34px;font-weight:300;color:#555b61}
.how p{position:absolute;left:620px;width:410px;font-size:10.5px;line-height:1.6;color:var(--ink-soft)}

/* testimonials */
.testimonials{position:absolute;left:0;top:1530px;width:1200px;height:350px;background:var(--grey-bg)}
.testimonials h2{position:absolute;left:0;top:40px;width:1200px;text-align:center;font-size:28px;font-weight:400;color:#5a5f64}
.t-card{position:absolute;top:120px;height:150px;background:var(--white);border-radius:2px;padding:22px 20px}
.t-photo{position:absolute;left:20px;top:28px;width:60px;height:60px;border-radius:50%;background:linear-gradient(180deg,#c7b6a5,#8e7c6b)}
.t-text{font-size:10px;line-height:1.6;color:var(--ink-soft)}
.t-name{margin-top:8px;font-size:10px;font-weight:600;color:#43484d}
.t-arrow{position:absolute;top:188px;width:14px;height:14px}

/* footer */
.site-footer{position:absolute;left:0;top:1880px;width:1200px;height:284px;background:var(--footer)}
.f-col{position:absolute;top:40px}
.f-col h4{font-family:"Raleway",sans-serif;font-size:13px;font-weight:600;color:var(--white);letter-spacing:.5px;margin-bottom:12px}
.f-col li{list-style:none;font-size:10.5px;color:var(--footer-text);line-height:2}
.socials{display:flex;gap:6px;margin-top:8px}
.socials span{width:20px;height:20px;border-radius:50%;border:1px solid var(--footer-text)}
.f-brand{position:absolute;left:870px;top:50px;width:190px;text-align:center}
.f-brand .brand-dot{margin:0 auto 10px;width:46px;height:46px;background:#6f7276}
.f-brand .brand-name{font-size:19px;color:#8e9195}
.f-rule{position:absolute;left:180px;top:235px;width:840px;height:1px;background:#3d3d40}
.copyright{position:absolute;left:180px;top:250px;font-size:9.5px;color:#7c7e82}
</style>
</head>
<body>

<header class="site-header">
  <div class="brand"><span class="brand-dot"></span><span class="brand-name">Transfer Tortoise</span></div>
  <nav class="main-nav">
    <span class="active">HOME</span><span>ABOUT US</span><span>CONTACT US</span><span>BLOG</span><span>BENEFITS</span>
  </nav>
  <span class="btn-support">SUPPORT</span>
  <span class="btn-login">LOG IN</span>
</header>

<section class="hero">
  <h1 class="hero-title"><span class="line1">Cloud based Online</span><span class="line2">Email MigrationService</span></h1>
  <p class="hero-copy">Move every mailbox with its settings and attachments to the new system, fully online, with no downtime for your users.</p>
  <span class="btn-outline">Learn More</span>
  <div class="hero-laptop" role="img" aria-label="Laptop showing the migration dashboard"></div>
  <div class="hero-planes" role="img" aria-label="Paper planes flying across the sky"></div>
  <div class="cloud-bank" role="img" aria-label="Bank of white clouds along the bottom of the sky"></div>
</section>

<section class="features">
  <div class="feature" style="left:200px">
    <div class="feature-icon">
      <svg width="34" height="34" viewBox="0 0 34 34" fill="none" stroke="#8a9097" stroke-width="2"><rect x="8" y="15" width="18" height="14" rx="2"/><path d="M12 15v-4a5 5 0 0 1 10 0v4"/><circle cx="17" cy="22" r="1.5" fill="#8a9097"/></svg>
    </div>
    <h3>Cloud Secure</h3>
    <p>Your mail stays encrypted in transit and at rest from start to final switch over.</p>
  </div>
  <div class="feature" style="left:480px">
    <div class="feature-icon">
      <svg width="34" height="34" viewBox="0 0 34 34" fill="none" stroke="#8a9097" stroke-width="2"><circle cx="17" cy="17" r="5"/><path d="M17 4v5M17 25v5M4 17h5M25 17h5M8 8l3.5 3.5M22.5 22.5L26 26M8 26l3.5-3.5M22.5 11.5L26 8"/></svg>
    </div>
    <h3>Easy to Access</h3>
    <p>Log in from any browser and run each migration without installing any tools.</p>
  </div>
  <div class="feature" style="left:760px">
    <div class="feature-icon">
      <svg width="34" height="34" viewBox="0 0 34 34" fill="none" stroke="#8a9097" stroke-width="2"><path d="M7 20v-4a10 10 0 0 1 20 0v4"/><rect x="5" y="19" width="5" height="8" rx="1"/><rect x="24" y="19" width="5" height="8" rx="1"/><path d="M26 27q0 3-6 3"/></svg>
    </div>
    <h3>Premium Support</h3>
    <p>Our migration team helps you plan and check every move, day or night.</p>
  </div>
</section>

<section class="migrate">
  <h2>What We Migrate</h2>
  <p style="top:140px">We move Kelvarn Postbox mailboxes with every folder, rule, contact, calendar and attachment intact, from one system to the next.</p>
  <p style="top:186px">Pick only the data you need, check the integrity of each item moved and repair damaged mail on the way. Data is synced over the weeks before your final date.</p>
  <p style="top:236px">Pay only for what you use by card or CoinDrift.</p>
  <span class="btn-outline">READ MORE</span>
  <div class="migrate-screen" role="img" aria-label="Desktop monitor showing a mailbox migration in progress"></div>
</section>

<section class="how">
  <div class="how-diagram" role="img" aria-label="Cloud connected to computers, phones and servers"></div>
  <h2>How it Works</h2>
  <p style="top:150px">Connect your source and target systems, choose the mailboxes and let the service copy them in the background while users keep working.</p>
  <p style="top:202px">A final sync then lets you switch over at once. End users can test the new system with their own mail before the switch date to make sure it all works.</p>
</section>

<section class="testimonials">
  <h2>Client Testimonials</h2>
  <div class="t-card" style="left:170px;width:210px">
    <p class="t-text">We moved three hundred mailboxes over a weekend and not one user lost access to their mail.</p>
    <p class="t-name">Daniel Ross</p>
  </div>
  <svg class="t-arrow" style="left:390px" viewBox="0 0 14 14" fill="none" stroke="#9aa0a6" stroke-width="2"><path d="M9 2L4 7l5 5"/></svg>
  <div class="t-card" style="left:415px;width:370px;padding-left:100px">
    <div class="t-photo" role="img" aria-label="Client portrait"></div>
    <p class="t-text">The staged sync meant our staff could test the new system with real mail first. The switch was quick, clean and painless.</p>
    <p class="t-name">Laura Benton</p>
  </div>
  <svg class="t-arrow" style="left:797px" viewBox="0 0 14 14" fill="none" stroke="#9aa0a6" stroke-width="2"><path d="M5 2l5 5-5 5"/></svg>
  <div class="t-card" style="left:825px;width:230px;padding-left:100px">
    <div class="t-photo" role="img" aria-label="Client portrait"></div>
    <p class="t-text">Simple pricing and a great team to help.</p>
    <p class="t-name">Mark Ellis</p>
  </div>
</section>

<footer class="site-footer">
  <div class="f-col" style="left:190px"><h4>COMPANY</h4><ul><li>Home</li><li>About Us</li><li>Benefits</li><li>Careers</li></ul></div>
  <div class="f-col" style="left:350px"><h4>FEATURES</h4><ul><li>Data Migration</li><li>Mail Sync</li><li>Integrity Check</li><li>Repair Tools</li></ul></div>
  <div class="f-col" style="left:520px"><h4>PRICING</h4><ul><li>Plans</li><li>Quotes</li><li>Free Trial</li></ul></div>
  <div class="f-col" style="left:680px"><h4>RESOURCES</h4><ul><li>Support</li><li>Blog</li><li>Contact Us</li></ul>
    <div class="socials"><span></span><span></span><span></span><span></span></div>
  </div>
  <div class="f-brand"><div class="brand-dot"></div><div class="brand-name">Transfer Tortoise</div></div>
  <div class="f-rule"></div>
  <p class="copyright">© 2014 Transfer Tortoise. All rights reserved.</p>
</footer>

</body>
</html>
```